Fashion Label Startup Business Card Design

Marianne Velk is a startup fashion designer based on the Gold Coast in QLD Australia. Mariannes label " Sorrina by Velk " is based upon taking old world design techniques and infusing them modern twist. The card design should incorporate an old world theme using colours like mustard, ocha, black, white and elements of lace pattern.

Card Details:

Marianne Velk
Fashion Designer
P: 04 0163 5271
E: sorrinabyvelk@mailbrook.net
W: www.threadpage.net/SOrrinaByVelk

```html
<!DOCTYPE html>
<html lang="en">
<head>
<meta charset="utf-8">
<title>Sorrina by Velk – Business Card</title>
<link rel="stylesheet" href="https://fonts.googleapis.com/css2?family=Great+Vibes&family=Libre+Baskerville:ital,wght@0,400;1,400&display=swap">
<style>
  :root {
    --backdrop: #7d766e;
    --cream: #f3e4c6;
    --cream-deep: #e9d3ad;
    --floral-peach: #e6c9a4;
    --khaki: #a08e70;
    --khaki-deep: #8a7658;
    --ink-black: #231c18;
    --mocha: #8b6a4f;
    --lace-white: #faf8f2;
    --text-dark: #2a2420;
  }
  * { margin: 0; padding: 0; box-sizing: border-box; }
  html, body { width: 1200px; height: 1000px; overflow: hidden; }
  body { background: var(--backdrop); position: relative; font-family: "Libre Baskerville", Georgia, serif; }

  .card {
    position: absolute;
    width: 722px;
    height: 440px;
    overflow: hidden;
    box-shadow: 0 4px 12px rgba(0,0,0,0.35);
  }
  .card--front { left: 110px; top: 45px; background: var(--cream); }
  .card--back  { left: 370px; top: 518px; }

  /* Front card bands */
  .band { position: absolute; left: 0; width: 100%; }
  .band--floral-top {
    top: 0; height: 190px;
    background: radial-gradient(circle at 70% 40%, var(--floral-peach), var(--cream) 60%), var(--cream);
  }
  .band--khaki {
    top: 175px; height: 140px;
    background: linear-gradient(90deg, var(--khaki), var(--khaki-deep) 50%, var(--khaki));
    clip-path: polygon(0 12%, 100% 0, 100% 100%, 0 100%);
  }
  .band--dark-floral {
    top: 350px; height: 90px;
    background: linear-gradient(90deg, var(--ink-black), #3a2c22 50%, var(--ink-black));
  }
  .lace {
    position: absolute; left: 0; width: 100%;
    background: linear-gradient(180deg, var(--lace-white), #e8e2d6 60%, rgba(250,248,242,0.6));
  }
  .lace--upper { top: 132px; height: 68px; clip-path: polygon(0 10%, 100% 0, 100% 88%, 0 100%); }
  .lace--lower { top: 302px; height: 98px; clip-path: polygon(0 0, 100% 4%, 100% 100%, 0 92%); }

  .brand-name {
    position: absolute; left: 28px; top: 50px;
    font-family: "Libre Baskerville", Georgia, serif;
    font-size: 58px; font-weight: 400;
    color: var(--text-dark);
    white-space: nowrap;
  }
  .tagline {
    position: absolute; left: 0; width: 100%; top: 262px;
    text-align: center;
    font-size: 36px; line-height: 1; letter-spacing: 1.5px;
    color: var(--lace-white);
    white-space: nowrap;
    z-index: 2;
  }

  /* Back card */
  .back-bg {
    position: absolute; inset: 0;
    background: radial-gradient(circle at 30% 40%, var(--cream-deep), var(--cream) 55%), var(--cream);
  }
  .lace-strip {
    position: absolute; inset: 0;
    background: linear-gradient(160deg, var(--lace-white), #e4ddcf);
    clip-path: polygon(86% 0, 100% 0, 100% 40%, 76% 100%, 63% 100%);
  }
  .designer-name {
    position: absolute; left: 38px; top: 40px;
    font-family: "Great Vibes", cursive;
    font-size: 96px; font-weight: 400; color: var(--mocha);
    white-space: nowrap;
  }
  .designer-role {
    position: absolute; left: 40px; top: 170px;
    font-size: 30px; font-weight: 400; letter-spacing: 1.5px;
    color: var(--text-dark);
  }
  .contact-list { position: absolute; left: 40px; top: 265px; list-style: none; }
  .contact-item {
    display: flex; align-items: center; gap: 13px;
    height: 30px; margin-bottom: 20.5px;
    font-style: italic; font-size: 19.5px; color: var(--text-dark);
    white-space: nowrap;
  }
  .contact-icon { width: 30px; height: 30px; flex: none; }
</style>
</head>
<body>

<section class="card card--front" aria-label="Business card front">
  <div class="band band--floral-top" role="img" aria-label="Cream and peach vintage floral pattern"></div>
  <div class="band band--khaki" role="img" aria-label="Khaki vintage floral pattern band"></div>
  <div class="band band--dark-floral" role="img" aria-label="Black floral pattern with peach roses"></div>
  <div class="lace lace--upper" role="img" aria-label="White scalloped lace trim"></div>
  <div class="lace lace--lower" role="img" aria-label="White floral guipure lace trim"></div>
  <h1 class="brand-name">Sorrina by Velk</h1>
  <p class="tagline">VINTAGE INSPIRED FASHION</p>
</section>

<section class="card card--back" aria-label="Business card back">
  <div class="back-bg" role="img" aria-label="Soft cream vintage floral pattern"></div>
  <div class="lace-strip" role="img" aria-label="Diagonal white floral lace ribbon"></div>
  <h2 class="designer-name">Marianne Velk</h2>
  <p class="designer-role">FASHION DESIGNER</p>
  <ul class="contact-list">
    <li class="contact-item">
      <svg class="contact-icon" viewBox="0 0 30 30" aria-hidden="true">
        <circle cx="15" cy="15" r="15" fill="#231c18"/>
        <path d="M8 13 q7-6 14 0 l-2 2 -3-1 v-1 q-2-1-4 0 v1 l-3 1z" fill="#f3e4c6"/>
        <rect x="10" y="15" width="10" height="7" rx="1.5" fill="#f3e4c6"/>
      </svg>
      <span>04 0163 5271</span>
    </li>
    <li class="contact-item">
      <svg class="contact-icon" viewBox="0 0 30 30" aria-hidden="true">
        <circle cx="15" cy="15" r="15" fill="#231c18"/>
        <rect x="8" y="10" width="14" height="10" fill="none" stroke="#f3e4c6" stroke-width="1.6"/>
        <path d="M8 10 l7 6 7-6" fill="none" stroke="#f3e4c6" stroke-width="1.6"/>
      </svg>
      <span>sorrinabyvelk@mailbrook.net</span>
    </li>
    <li class="contact-item">
      <svg class="contact-icon" viewBox="0 0 30 30" aria-hidden="true">
        <circle cx="15" cy="15" r="15" fill="#231c18"/>
        <path d="M11 8 l9 9 -4 0 2 5 -2 1 -2-5 -3 3z" fill="#f3e4c6"/>
      </svg>
      <span>www.threadpage.net/SOrrinaByVelk</span>
    </li>
  </ul>
</section>

</body>
</html>
```